Redo our website for our Robotics company

We sell robotic equipment to the restaurant industry. Our current robot, is a cooking robot that cooks up to 15 lbs of food. We will provide a prior website as well as brand guidelines. We plan on using wordpress and take advantage of wordpress's visual (no code) editor.

Current website - https://kelvatrix88.com/ (please note we are only selling Duffle now and no longer selling Pando+

We want someone to take our existing content and design the website as well as layout our content we provide. Here's a suggested site layout:

✅ KelvaTrix88 Website Wireframe / Site Map
1. Home

Purpose: Introduce Duffle, establish credibility, drive demo requests.

Sections:

Hero Section

Headline: “Meet Duffle — Your New Robotic Chef for High-Volume, Consistent Cooking.”

Sub-headline: Increase throughput. Reduce labor. Deliver perfect food every time.

CTA: Request a Demo + Watch Duffle Cook

Visual: Video loop or hero animation of Duffle in action.

How Duffle Works (3-4 steps)

Step cards: Load Ingredients → Select Recipe → Duffle Cooks → Serve

Icons and short explanations.

Key Benefits

Labor savings

Zero inconsistency

24/7 uptime

Throughput increases (30–50% faster)

Health & safety compliance

Who It’s For

QSR restaurants

Fast casual

Catering/commissaries

Ghost kitchens

Case Studies / Testimonials

Logo bar + quotes

“Duffle helped us reduce cooking times by 40%.”

Video Section

“Watch Duffle cook a full batch from start to finish.”

CTA Section

Big banner: Book a Demo

2. Product: “Meet Duffle”

Purpose: Deep dive into hardware, software, safety, reliability.

Sections:

Overview

What Duffle is

What tasks it automates

Where it fits in a kitchen

Hardware Features

High-temperature cooking chamber

Precision sensors

Automated stirring

Automated dispensing

Safety mechanisms (locking lids, auto-shutoff)

Software & AI

Recipe automation

IoT dashboard

Remote monitoring

Predictive maintenance

Specs Table

Dimensions

Power requirements

Capacity (lbs per batch)

Safety certifications

Gallery

Close-ups, installation photos, process shots

CTA: Request a Demo

3. Solutions

Purpose: Show that Duffle solves real operational problems.

Sub-pages or sections:

For Quick-Service Restaurants

Reduce labor cost

Speed up peak-hour demand

For Catering & Commissaries

Large-batch consistency

Automate repetitive cooking tasks

For High-Growth Chains

Replicable quality across multiple locations

Centralized recipe control

Each solution page includes:

A problem statement

How Duffle solves it

Metrics / KPIs

Relevant testimonial

CTA

4. ROI / Economics

Purpose: Sell the financial story clearly.

Sections:

Savings Calculator

Labor hours saved

Cost savings

Throughput increases

Food waste reduction

Before & After Comparison

Traditional kitchen vs. robotic kitchen

Sample ROI

“Payback in as little as 3–6 months.”

Download Full ROI Report (PDF)

5. Case Studies

Purpose: Social proof + real results.

Structure for each case study:

Customer background

Problem

Implementation

KPIs achieved

Labor savings

Consistency improvements

Cooking speed

Quote + photos/video

6. Pricing

Purpose: Start a commercial conversation.

Include:

Subscription model (monthly / annual)

Hardware leasing or purchase options

Installation + training

Support level

CTA to book a sales call

7. About

Purpose: Build trust.

Sections:

Mission statement

Founding team

Advisors/partners

“Why we built Duffle”

8. Resources

Purpose: SEO + education.

Subpages:

Blog (e.g., “The Future of Automated Kitchens”)

Whitepapers

Technical documentation

Product videos

9. Contact

General inquiry form

Sales contact

Support portal

Careers

```html
<!DOCTYPE html>
<html lang="en">
<head>
<meta charset="utf-8">
<title>KelvaTrix88 — Meet Duffle</title>
<link href="https://fonts.googleapis.com/css2?family=Outfit:wght@500;600;700&family=Poppins:wght@400;500;600&display=swap" rel="stylesheet">
<style>
:root{
  --red:#ee4a2f;
  --orange:#f6813d;
  --ink:#1c1c1c;
  --dark:#222222;
  --grey:#6b6b6b;
  --pill:#ececec;
  --white:#ffffff;
  --grad:linear-gradient(135deg,#f68a3f 0%,#ee4a2f 60%,#e63a2a 100%);
}
*{box-sizing:border-box;margin:0;padding:0}
html,body{width:1200px;height:3822px;overflow:hidden}
body{position:relative;background:var(--white);font-family:'Poppins',sans-serif;color:var(--ink)}
.abs{position:absolute}
.display{font-family:'Outfit',sans-serif;font-weight:700;letter-spacing:-0.5px}
.accent{color:var(--red)}
.glow{position:absolute;border-radius:50%;filter:blur(60px);pointer-events:none}

/* slanted buttons */
.btn{position:absolute;display:flex;align-items:center;justify-content:center;font-family:'Poppins',sans-serif;font-weight:600;font-size:10px;letter-spacing:.2px;text-transform:uppercase}
.btn::before{content:"";position:absolute;inset:0;transform:skewX(-18deg);border-radius:10px;z-index:0}
.btn span{position:relative;z-index:1}
.btn-primary{color:var(--white)}
.btn-primary::before{background:var(--grad)}
.btn-outline{color:var(--ink)}
.btn-outline::before{border:1.5px solid var(--ink);background:var(--white)}
.btn-light{color:var(--ink)}
.btn-light::before{background:var(--white)}

/* header */
.brand{font-family:'Outfit',sans-serif;font-weight:700;color:var(--red)}
.nav{position:absolute;left:382px;top:44px;display:flex;gap:26px;align-items:center;font-size:10.5px;font-weight:600;text-transform:uppercase}

/* hero */
.hero-title{left:104px;top:226px;font-size:46px;line-height:50px;width:480px}
.hero-sub{left:104px;top:446px;font-size:17px;line-height:27px;width:360px}
.hero-visual{left:516px;top:119px;width:684px;height:571px;border-radius:300px 0 0 260px/340px 0 0 300px;background:linear-gradient(160deg,#3d3a38 0%,#8c8b89 45%,#c9c8c5 70%,#6e6c69 100%)}

/* steps */
.section-title{font-size:38px;text-align:center;width:1200px;left:0}
.step{position:absolute;width:190px;height:190px;border-radius:50%;background:var(--white);border:10px solid #f1f1f1;box-shadow:0 8px 22px rgba(0,0,0,.08);display:flex;flex-direction:column;align-items:center;justify-content:center;text-align:center}
.step h3{font-family:'Outfit',sans-serif;font-weight:600;font-size:15px;line-height:18px;margin-bottom:8px}
.step p{font-size:11px;line-height:15px;color:var(--grey);width:120px}
.step-badge{position:absolute;width:50px;height:50px;border-radius:50%;display:flex;align-items:center;justify-content:center;border:3px solid var(--white);box-shadow:0 4px 10px rgba(0,0,0,.12)}
.badge-red{background:var(--grad)}
.badge-dark{background:var(--ink)}
.step-arrow{position:absolute}

/* benefits */
.benefit-list{position:absolute;left:291px;top:1208px;width:328px}
.benefit{height:41px;border-radius:21px;display:flex;align-items:center;padding-left:20px;font-size:12.5px;gap:8px;margin-bottom:1px}
.benefit.shaded{background:var(--pill)}
.tick{width:12px;height:12px;border-radius:50%;background:var(--red);display:inline-flex;align-items:center;justify-content:center}

/* audience */
.audience{left:0;top:1568px;width:1093px;height:501px;background:var(--dark);border-radius:0 220px 320px 0/0 170px 420px 0;overflow:hidden}
.audience-visual{position:absolute;right:0;top:0;width:640px;height:501px;background:linear-gradient(90deg,rgba(34,34,34,1) 0%,rgba(90,88,86,.7) 45%,rgba(150,148,145,.55) 100%)}
.aud-card{position:absolute;top:1741px;width:217px;height:217px;border-radius:28px;background:var(--white);display:flex;flex-direction:column;align-items:center;justify-content:center;text-align:center;font-family:'Outfit',sans-serif;font-weight:600;font-size:18px;line-height:21px;box-shadow:0 10px 30px rgba(0,0,0,.2)}
.aud-card svg{margin-bottom:18px}
.aud-card.featured{background:var(--grad);color:var(--white)}

/* video */
.video-visual{left:190px;top:2164px;width:427px;height:427px;border-radius:64px;background:linear-gradient(150deg,#5d5955 0%,#a9a7a3 40%,#d8d6d2 65%,#7b7874 100%)}
.play{left:277px;top:2543px;width:92px;height:92px;border-radius:50%;background:var(--grad);border:4px solid var(--white);box-shadow:0 8px 20px rgba(238,74,47,.35);display:flex;align-items:center;justify-content:center}
.video-title{left:678px;top:2270px;font-size:38px;line-height:47px;width:440px}

/* logos */
.logo-chip{position:absolute;top:2819px;width:116px;height:116px;border-radius:50%;background:var(--white);box-shadow:0 6px 16px rgba(0,0,0,.1);display:flex;align-items:center;justify-content:center;font-family:'Poppins',sans-serif;font-weight:500;font-size:15px;color:#333}
.quote{left:0;width:1200px;text-align:center;top:3003px;font-family:'Outfit',sans-serif;font-weight:500;font-size:26px}
.cite{left:0;width:1200px;text-align:center;top:3047px;font-size:12px;font-weight:600;color:var(--red)}
.dots{left:576px;top:3094px;display:flex;gap:11px}
.dots i{width:8px;height:8px;border-radius:50%;background:var(--ink);display:block}
.dots i.on{background:var(--red)}

/* cta + footer */
.footer{left:0;top:3296px;width:1200px;height:526px;background:linear-gradient(160deg,#1a1a1a 0%,#161616 60%,#2a1510 100%)}
.cta{left:89px;top:3186px;width:1020px;height:215px}
.cta-title{left:212px;top:3230px;font-size:37px;line-height:46px;color:var(--white)}
.cta-text{left:212px;top:3335px;font-size:11px;color:var(--white)}
.foot-h{font-family:'Outfit',sans-serif;font-weight:600;font-size:18px;color:var(--white)}
.foot-links{font-size:11.5px;line-height:21px;color:#d8d8d8;list-style:none}
.foot-small{font-size:11.5px;line-height:18px;color:#d8d8d8}
.social{position:absolute;top:3595px;width:40px;height:40px;border-radius:50%;background:#333;display:flex;align-items:center;justify-content:center;font-size:8.5px;color:var(--white);font-weight:500}
.rule{left:104px;top:3763px;width:992px;height:1px;background:#3a3a3a}
.chat{left:1121px;top:3740px;width:48px;height:48px;border-radius:50%;background:var(--grad);box-shadow:0 0 0 5px rgba(238,74,47,.25);display:flex;align-items:center;justify-content:center}
</style>
</head>
<body>

<!-- soft background tints -->
<div class="glow" style="left:-160px;top:380px;width:420px;height:420px;background:rgba(246,160,120,.28)"></div>
<div class="glow" style="left:620px;top:1420px;width:520px;height:200px;background:rgba(246,160,130,.22)"></div>
<div class="glow" style="left:40px;top:2500px;width:520px;height:300px;background:rgba(246,170,140,.18)"></div>
<div class="glow" style="left:860px;top:2300px;width:360px;height:400px;background:rgba(246,170,140,.2)"></div>

<!-- header -->
<header>
  <div class="abs brand" style="left:104px;top:34px;font-size:32px;line-height:40px">KelvaTrix88</div>
  <nav class="nav">
    <svg width="14" height="13" viewBox="0 0 14 13"><path d="M7 0 0 6h2v7h4V9h2v4h4V6h2z" fill="#ee4a2f"/></svg>
    <span>Product</span><span>Solutions</span><span>Case Studies</span><span>Pricing</span><span>About</span><span>Resources</span><span>Contact</span>
  </nav>
  <a class="btn btn-primary" style="left:962px;top:30px;width:128px;height:41px"><span>Request a Demo</span></a>
</header>

<!-- hero -->
<section>
  <h1 class="abs display hero-title">Meet Duffle — Your New <span class="accent">Robotic Chef</span> for High-Volume, Consistent Cooking.</h1>
  <p class="abs hero-sub">Increase throughput. Reduce labor. Deliver perfect food every time.</p>
  <a class="btn btn-primary" style="left:110px;top:527px;width:134px;height:44px"><span>Request a Demo</span></a>
  <a class="btn btn-outline" style="left:250px;top:527px;width:160px;height:44px"><span>▶ Watch Duffle Cook</span></a>
  <div class="abs hero-visual" role="img" aria-label="Row of stainless steel Duffle cooking robots with a wok tossing a stir-fry"></div>
</section>

<!-- how it works -->
<section>
  <h2 class="abs display section-title" style="top:745px">How Duffle Works</h2>

  <div class="step" style="left:148px;top:825px"><h3>1. Load<br>Ingredients</h3><p>Lorem ipsum proin gravida nibh vel.</p></div>
  <div class="step" style="left:383px;top:825px"><h3>2. Select<br>Recipe</h3><p>Lorem ipsum proin gravida nibh vel.</p></div>
  <div class="step" style="left:617px;top:825px"><h3>3. Duffle<br>Cooks</h3><p>Lorem ipsum proin gravida nibh vel.</p></div>
  <div class="step" style="left:854px;top:825px"><h3>4. Serve</h3><p>Lorem ipsum proin gravida nibh vel.</p></div>

  <div class="step-badge badge-red" style="left:284px;top:834px"><svg width="22" height="22" viewBox="0 0 22 22" fill="none" stroke="#fff" stroke-width="1.8"><path d="M3 9h16l-2 9H5z"/><path d="M7 9l4-6 4 6"/></svg></div>
  <div class="step-badge badge-dark" style="left:518px;top:834px"><svg width="20" height="22" viewBox="0 0 20 22" fill="none" stroke="#fff" stroke-width="1.8"><rect x="3" y="2" width="14" height="18" rx="2"/><circle cx="10" cy="9" r="3"/><path d="M7 15h6"/></svg></div>
  <div class="step-badge badge-red" style="left:753px;top:834px"><svg width="22" height="22" viewBox="0 0 22 22" fill="none" stroke="#fff" stroke-width="1.8"><path d="M6 13a4 4 0 1 1 2-7 4 4 0 0 1 6 0 4 4 0 1 1 2 7v5H6z"/><path d="M6 15h10"/></svg></div>
  <div class="step-badge badge-dark" style="left:990px;top:834px"><svg width="24" height="22" viewBox="0 0 24 22" fill="none" stroke="#fff" stroke-width="1.8"><path d="M3 15a9 9 0 0 1 18 0z"/><path d="M2 18h20"/><circle cx="12" cy="5" r="1.2"/></svg></div>

  <svg class="step-arrow" style="left:336px;top:905px" width="48" height="20" viewBox="0 0 48 20" fill="none" stroke="#bdbdbd" stroke-width="2"><path d="M2 10h42M36 3l8 7-8 7"/></svg>
  <svg class="step-arrow" style="left:570px;top:905px" width="48" height="20" viewBox="0 0 48 20" fill="none" stroke="#bdbdbd" stroke-width="2"><path d="M2 10h42M36 3l8 7-8 7"/></svg>
  <svg class="step-arrow" style="left:805px;top:905px" width="48" height="20" viewBox="0 0 48 20" fill="none" stroke="#bdbdbd" stroke-width="2"><path d="M2 10h42M36 3l8 7-8 7"/></svg>
</section>

<!-- key benefits -->
<section>
  <div class="abs brand" style="left:218px;top:1450px;font-size:52px;line-height:60px;transform:rotate(-90deg);transform-origin:0 0;white-space:nowrap">KelvaTrix88</div>
  <h2 class="abs display" style="left:300px;top:1138px;font-size:38px">Key Benefits</h2>
  <ul class="benefit-list" style="list-style:none">
    <li class="benefit shaded"><span class="tick"><svg width="7" height="6" viewBox="0 0 7 6"><path d="M1 3l2 2 3-4" stroke="#fff" stroke-width="1.4" fill="none"/></svg></span>Labor savings</li>
    <li class="benefit"><span class="tick"><svg width="7" height="6" viewBox="0 0 7 6"><path d="M1 3l2 2 3-4" stroke="#fff" stroke-width="1.4" fill="none"/></svg></span>Zero inconsistency</li>
    <li class="benefit shaded"><span class="tick"><svg width="7" height="6" viewBox="0 0 7 6"><path d="M1 3l2 2 3-4" stroke="#fff" stroke-width="1.4" fill="none"/></svg></span>24/7 uptime</li>
    <li class="benefit"><span class="tick"><svg width="7" height="6" viewBox="0 0 7 6"><path d="M1 3l2 2 3-4" stroke="#fff" stroke-width="1.4" fill="none"/></svg></span>Throughput increases (30–50% faster)</li>
    <li class="benefit shaded"><span class="tick"><svg width="7" height="6" viewBox="0 0 7 6"><path d="M1 3l2 2 3-4" stroke="#fff" stroke-width="1.4" fill="none"/></svg></span>Health &amp; safety compliance</li>
  </ul>
  <div class="abs" role="img" aria-label="Single Duffle cooking robot standing on an orange pedestal" style="left:676px;top:1080px;width:340px;height:403px">
    <div class="abs" style="left:0;top:290px;width:340px;height:113px;border-radius:50%/40%;background:linear-gradient(180deg,#f6813d,#e33c27)"></div>
    <div class="abs" style="left:90px;top:0;width:180px;height:330px;border-radius:14px;background:linear-gradient(135deg,#2f2f2f 0%,#777 45%,#c8c8c6 75%,#555 100%)"></div>
  </div>
</section>

<!-- who it's for -->
<section>
  <div class="abs audience"><div class="audience-visual" role="img" aria-label="Dimmed row of Duffle cooking robots in a commercial kitchen"></div></div>
  <h2 class="abs display" style="left:139px;top:1664px;font-size:36px;color:var(--white)">Who It’s For</h2>

  <div class="aud-card" style="left:139px">
    <svg width="70" height="70" viewBox="0 0 70 70" fill="none" stroke="#1c1c1c" stroke-width="2.2"><circle cx="35" cy="35" r="32"/><circle cx="35" cy="35" r="20"/><path d="M14 18v14M18 18v14M22 18v14M14 32h8M18 32v22"/><path d="M52 18c-5 4-5 14 0 16v20"/></svg>
    QSR<br>Restaurants</div>
  <div class="aud-card featured" style="left:373px">
    <svg width="70" height="70" viewBox="0 0 70 70" fill="none" stroke="#fff" stroke-width="2.2"><path d="M6 38a16 14 0 0 1 32 0z"/><path d="M6 44h32M7 50h30a3 3 0 0 1-3 5H10a3 3 0 0 1-3-5z"/><path d="M42 24h18l-3 40H45z"/><path d="M51 24V10l6-4"/></svg>
    Fast<br>Casual</div>
  <div class="aud-card" style="left:608px">
    <svg width="80" height="70" viewBox="0 0 80 70" fill="none" stroke="#1c1c1c" stroke-width="2.2"><circle cx="40" cy="16" r="10"/><path d="M8 36h64v8H8zM12 44v20h56V44M20 48v14M28 48v14M36 48v14M44 48v14M52 48v14M60 48v14M30 36V28h20v8"/></svg>
    Catering<br>Commissaries</div>
  <div class="aud-card" style="left:844px">
    <svg width="80" height="70" viewBox="0 0 80 70" fill="none" stroke="#1c1c1c" stroke-width="2.2"><path d="M34 14h12l4 8H30z" fill="#ee4a2f" stroke="#ee4a2f"/><path d="M40 14V6"/><path d="M6 28h68v36H6zM6 40h68M30 28v36M40 50h24M40 56h24"/><circle cx="18" cy="34" r="2"/></svg>
    Ghost<br>Kitchens</div>
</section>

<!-- video -->
<section>
  <div class="abs video-visual" role="img" aria-label="Duffle robots plating cooked noodles onto dishes"></div>
  <div class="abs play"><svg width="18" height="20" viewBox="0 0 18 20"><path d="M2 1l15 9-15 9z" fill="#fff"/></svg></div>
  <h2 class="abs display video-title">Watch Duffle Cook a <span class="accent">Full Batch</span> from Start to Finish.</h2>
  <a class="btn btn-outline" style="left:684px;top:2434px;width:164px;height:46px"><span>▶ Watch Duffle Cook</span></a>
</section>

<!-- case studies -->
<section>
  <h2 class="abs display section-title" style="top:2718px">Case Studies &amp; Testimonials</h2>
  <p class="abs" style="left:0;width:1200px;text-align:center;top:2772px;font-size:12.5px">Real kitchens. Real results. Real efficiency.</p>

  <svg class="abs" style="left:78px;top:2868px" width="14" height="18" viewBox="0 0 14 18" fill="none" stroke="#1c1c1c" stroke-width="2"><path d="M10 2 3 9l7 7"/></svg>
  <svg class="abs" style="left:1108px;top:2868px" width="14" height="18" viewBox="0 0 14 18" fill="none" stroke="#1c1c1c" stroke-width="2"><path d="M4 2l7 7-7 7"/></svg>

  <div class="logo-chip" style="left:153px">Norvale</div>
  <div class="logo-chip" style="left:283px">Hostwell</div>
  <div class="logo-chip" style="left:414px">Fizzora</div>
  <div class="logo-chip" style="left:544px">Brightmoor</div>
  <div class="logo-chip" style="left:673px">Mealcrest</div>
  <div class="logo-chip" style="left:804px">Dinerly</div>
  <div class="logo-chip" style="left:934px">Wingstead</div>

  <p class="abs quote">“Duffle helped us reduce cooking times by 40%”</p>
  <p class="abs cite">— Operations Manager, QSR Chain</p>
  <div class="abs dots"><i></i><i class="on"></i><i></i></div>
</section>

<!-- footer with CTA -->
<footer>
  <div class="abs footer"></div>
  <svg class="abs cta" viewBox="0 0 1020 215" preserveAspectRatio="none" aria-hidden="true">
    <defs><linearGradient id="ctaGrad" x1="0" y1="0" x2="1" y2="1"><stop offset="0" stop-color="#f6883e"/><stop offset=".6" stop-color="#ee4a2f"/><stop offset="1" stop-color="#e5392a"/></linearGradient></defs>
    <path d="M105 0H990q40 0 24 36L944 190q-12 25-40 25H30Q-10 215 6 180L78 22Q88 0 105 0z" fill="url(#ctaGrad)"/>
  </svg>
  <h2 class="abs display cta-title">Book Your Demo Today and<br>See Duffle in Action!</h2>
  <p class="abs cta-text">Experience high-volume, consistent cooking with zero hassle. Schedule a live demo now.</p>
  <a class="btn btn-light" style="left:822px;top:3270px;width:162px;height:48px"><span>Request a Demo</span></a>

  <div class="abs brand" style="left:101px;top:3530px;font-size:58px;line-height:66px">KelvaTrix88</div>
  <p class="abs" style="left:101px;width:338px;text-align:center;top:3619px;font-family:'Outfit',sans-serif;font-weight:600;font-size:18px;color:var(--white)">Enhance, Not Replace.</p>

  <div class="abs" style="left:516px;top:3486px">
    <h4 class="foot-h">Company</h4>
    <ul class="foot-links" style="margin-top:16px"><li>Product</li><li>Solutions</li><li>Case Studies</li><li>Pricing</li><li>About</li><li>Resources</li><li>Contact</li></ul>
  </div>

  <div class="abs" style="left:678px;top:3486px;width:190px">
    <h4 class="foot-h">Contact</h4>
    <div class="foot-small" style="margin-top:16px;display:flex;gap:8px">
      <svg width="11" height="9" viewBox="0 0 11 9" style="margin-top:5px"><rect width="11" height="9" rx="1" fill="#ee4a2f"/><path d="M0 1l5.5 4L11 1" stroke="#1a1a1a" fill="none"/></svg>
      <span>Email:<br>info@kelvatrix88.com</span></div>
    <div class="foot-small" style="margin-top:14px;display:flex;gap:8px">
      <svg width="11" height="11" viewBox="0 0 11 11" style="margin-top:4px"><path d="M2 0l2 2-1 2a6 6 0 0 0 4 4l2-1 2 2-2 2C4 11 0 7 0 2z" fill="#ee4a2f"/></svg>
      <span>Phone:<br>+1 (555) 014 2290</span></div>
  </div>

  <div class="abs" style="left:882px;top:3486px;width:214px">
    <h4 class="foot-h">Newsletter</h4>
    <div style="margin-top:22px;border-bottom:1px solid #555;padding-bottom:8px;display:flex;justify-content:space-between;font-size:11px;color:#888">
      <span>Enter email address</span>
      <svg width="12" height="12" viewBox="0 0 12 12"><path d="M0 5 12 0 7 12 5 7z" fill="#ee4a2f"/></svg>
    </div>
  </div>
  <div class="social" style="left:885px">Loop</div>
  <div class="social" style="left:934px">Pipit</div>
  <div class="social" style="left:983px">Frame</div>

  <div class="abs rule"></div>
  <p class="abs foot-small" style="left:0;width:1200px;text-align:center;top:3783px;font-size:11px">KelvaTrix88 © 2025. All Rights Reserved.</p>
  <p class="abs foot-small" style="left:900px;top:3783px;font-size:11px">Privacy Policy &nbsp;&nbsp;|&nbsp;&nbsp; Terms of Service</p>

  <div class="abs chat"><svg width="22" height="20" viewBox="0 0 22 20"><path d="M3 2h16a2 2 0 0 1 2 2v9a2 2 0 0 1-2 2H9l-5 4v-4H3a2 2 0 0 1-2-2V4a2 2 0 0 1 2-2z" fill="#fff"/><circle cx="7" cy="9" r="1.3" fill="#ee4a2f"/><circle cx="11" cy="9" r="1.3" fill="#ee4a2f"/><circle cx="15" cy="9" r="1.3" fill="#ee4a2f"/></svg></div>
</footer>

</body>
</html>
```